Business Card/Email Signature design

We need an new business card design for our business as well as an animated email signature design.<br/>Business Card:<br/>The business card designs need to have the following information for each director:<br/>Glen Purvis<br/>Managing Director<br/>glen@fernloxstaffing.com.au<br/>0468203917<br/>www.fernloxstaffing.com.au<br/><br/>and<br/><br/>Rosalind Tremby<br/>Director<br/>rosalind@fernloxstaffing.com.au<br/>0457390264<br/>www.fernloxstaffing.com.au<br/><br/>I will upload the Fernlox. Staffing logo designs to be used for the design. Our colours are black and white. I would like to see the designs in both coloured backgrounds.<br/><br/>For the email signature we need the same information. I also need to add a logo of our association NPLB of which i will add the logo as well. This NPLB logo does not need to be used for the business card unless it works with the design.<br/>For the animation part of the logo our company is called Fernlox. Staffing - We have a number of divisions called Fernlox. Construct, Fernlox. Property, Fernlox. Sales, Fernlox. Executive Support, Fernlox. Private PA, Fernlox. Talent and Fernlox. Coaching<br/>I would like for the email Signature to be designed so that the Fernlox. stays still but the words Construct, Property, Sales, Executive Support, Private PA, Talent and Coaching rotate through to capture attention and tell the story of what we do.<br/><br/>Any questions please don't hesitate to message me.

Industry/Entity Type

Recruiter

Contact Information for Business Card

Glen Purvis
Managing Director
glen@fernloxstaffing.com.au
0468203917
www.fernloxstaffing.com.au

Rosalind Tremby
Director
rosalind@fernloxstaffing.com.au
0457390264
www.fernloxstaffing.com.au

Font styles to use
Serif

Colors

Designer to choose colors to be used in the design.

Requirements
Must have
• The animation for the email signature as described
Should not have
• Any changes to my logo. Any colour other that black or white

```html
<!DOCTYPE html>
<html lang="en">
<head>
<meta charset="utf-8">
<title>Fernlox. Staffing — Business Card</title>
<link rel="stylesheet" href="https://fonts.googleapis.com/css2?family=Lato:wght@400;700&display=swap">
<style>
  :root {
    --page-bg: #e6e2dc;
    --card-frost: #d9d3ca;
    --card-edge: #c6bfb4;
    --panel-dark: #121212;
    --panel-mid: #2a2a2a;
    --panel-shadow: #8d8a85;
    --name-ink: #dcd0bb;
    --detail-ink: #b9b1a3;
    --brand-ink: #1a1a1a;
  }
  * { margin: 0; padding: 0; box-sizing: border-box; }
  html, body {
    width: 1200px;
    height: 1047px;
    overflow: hidden;
    background: var(--page-bg);
  }
  .business-card {
    position: absolute;
    left: 100px;
    top: 251px;
    width: 1000px;
    height: 544px;
    border-radius: 26px;
    overflow: hidden;
    background: linear-gradient(135deg, #ded8cf 0%, var(--card-frost) 60%, #cfc8bd 100%);
    border: 1px solid var(--card-edge);
    font-family: "Lato", sans-serif;
  }
  .card-shape {
    position: absolute;
    inset: 0;
    width: 100%;
    height: 100%;
  }
  .contact-block {
    position: absolute;
    left: 34px;
    top: 0;
    width: 500px;
    height: 100%;
  }
  .person-name {
    position: absolute;
    top: 78px;
    font-size: 41px;
    font-weight: 700;
    color: var(--name-ink);
    letter-spacing: 0.2px;
  }
  .person-role {
    position: absolute;
    top: 133px;
    font-size: 24px;
    font-weight: 400;
    color: var(--detail-ink);
  }
  .address {
    position: absolute;
    top: 258px;
    font-size: 25px;
    line-height: 32px;
    color: var(--detail-ink);
  }
  .contact-list {
    position: absolute;
    top: 348px;
    list-style: none;
  }
  .contact-list li {
    display: flex;
    align-items: center;
    height: 37px;
    font-size: 25px;
    color: var(--detail-ink);
  }
  .contact-icon {
    width: 26px;
    height: 26px;
    margin-right: 22px;
    flex: none;
  }
  .brand-name {
    position: absolute;
    left: 600px;
    width: 340px;
    top: 246px;
    text-align: center;
    font-size: 40px;
    font-weight: 700;
    color: var(--brand-ink);
    letter-spacing: 0.5px;
  }
</style>
</head>
<body>
  <div class="business-card">
    <svg class="card-shape" viewBox="0 0 1000 544" aria-hidden="true">
      <defs>
        <linearGradient id="panel-fill" x1="0" y1="0" x2="1" y2="1">
          <stop offset="0" stop-color="var(--panel-mid)"/>
          <stop offset="0.55" stop-color="var(--panel-dark)"/>
          <stop offset="1" stop-color="#1d1d1d"/>
        </linearGradient>
        <linearGradient id="edge-fill" x1="0" y1="0" x2="1" y2="0">
          <stop offset="0" stop-color="var(--panel-shadow)"/>
          <stop offset="1" stop-color="#c9c3b9"/>
        </linearGradient>
      </defs>
      <path class="panel-edge" d="M0 0 H556 C470 120 458 400 552 544 H0 Z" fill="url(#edge-fill)"/>
      <path class="panel-dark" d="M0 0 H549 C462 120 450 400 534 544 H0 Z" fill="url(#panel-fill)"/>
    </svg>

    <div class="contact-block">
      <h1 class="person-name">Glen Purvis</h1>
      <p class="person-role">Managing Director</p>
      <p class="address">1234 First Line Address<br>5678 Second Line Address</p>
      <ul class="contact-list">
        <li>
          <svg class="contact-icon" viewBox="0 0 24 24" aria-hidden="true">
            <path d="M6.6 10.8a15 15 0 0 0 6.6 6.6l2.2-2.2a1 1 0 0 1 1-.25 11.4 11.4 0 0 0 3.6.57 1 1 0 0 1 1 1V20a1 1 0 0 1-1 1A17 17 0 0 1 3 4a1 1 0 0 1 1-1h3.5a1 1 0 0 1 1 1c0 1.25.2 2.45.57 3.57a1 1 0 0 1-.25 1Z" fill="var(--detail-ink)"/>
          </svg>
          0468203917
        </li>
        <li>
          <svg class="contact-icon" viewBox="0 0 24 24" aria-hidden="true">
            <rect x="2" y="5" width="20" height="14" fill="var(--detail-ink)"/>
            <path d="M2.5 5.5 12 13l9.5-7.5M2.5 18.5 9 12m12.5 6.5L15 12" stroke="var(--panel-dark)" stroke-width="1.4" fill="none"/>
          </svg>
          glen@fernloxstaffing.com.au
        </li>
        <li>
          <svg class="contact-icon" viewBox="0 0 24 24" aria-hidden="true">
            <circle cx="12" cy="12" r="9.5" fill="none" stroke="var(--detail-ink)" stroke-width="1.6"/>
            <path d="M2.5 12h19M12 2.5c-3.5 3.5-3.5 15.5 0 19M12 2.5c3.5 3.5 3.5 15.5 0 19M4.5 7h15M4.5 17h15" stroke="var(--detail-ink)" stroke-width="1.3" fill="none"/>
          </svg>
          www.fernloxstaffing.com.au
        </li>
      </ul>
    </div>

    <p class="brand-name">Fernlox. Staffing</p>
  </div>
</body>
</html>
```